Complete the design for a website wireframe

I need someone to follow the attached wireframe and update the design including icons, pictures and graphics to compliment the copy. I want to have good transitions between sections. All items need to be included as separate files.

Target Market(s)

IT Executives

Number of Pages Required

3 page

Colors
0054AA
0677BA
7BADD7
CADEEF
E8F1F8
F0912C
F2A743
F7CA91
FBE8D2
FDF5EE

```html
<!DOCTYPE html>
<html lang="en">
<head>
<meta charset="UTF-8">
<title>SkyBridge Solutions – IT Advisory</title>
<link href="https://fonts.googleapis.com/css2?family=Outfit:wght@400;500;600;700&display=swap" rel="stylesheet">
<style>
:root{
  --blue-900:#0054AA;
  --blue-700:#0677BA;
  --blue-400:#7BADD7;
  --blue-200:#CADEEF;
  --blue-100:#E8F1F8;
  --orange:#F0912C;
  --orange-2:#F2A743;
  --peach:#FBE8D2;
  --ink:#111827;
  --muted:#4b5563;
  --navy:#1f2f4d;
  --white:#ffffff;
}
*{margin:0;padding:0;box-sizing:border-box}
html,body{width:1200px;height:2436px;overflow:hidden}
body{font-family:"Outfit",sans-serif;color:var(--ink);background:var(--white)}
.eyebrow{display:inline-block;background:var(--blue-100);border:1px solid var(--blue-200);color:#374151;font-size:14px;letter-spacing:3px;font-weight:500;padding:8px 22px;border-radius:4px;text-transform:uppercase}
.btn{display:inline-block;background:var(--blue-900);color:var(--white);font-weight:600;font-size:18px;padding:14px 30px;border-radius:6px}

/* partners */
.partners{height:220px;background:var(--blue-100);text-align:center;padding-top:56px}
.partners .eyebrow{background:var(--blue-200)}
.partner-row{display:flex;justify-content:center;gap:86px;margin-top:38px}
.partner{font-size:26px;font-weight:600;color:var(--blue-900)}

/* how */
.how{height:620px;text-align:center;padding-top:108px}
.how h2{font-size:52px;font-weight:700;margin-top:18px}
.how h2 em{font-weight:600}
.steps{display:flex;justify-content:center;gap:40px;margin:64px auto 0;width:1040px}
.step{width:320px}
.step svg{width:64px;height:64px}
.step h3{font-size:26px;font-weight:600;margin:12px 0 14px}
.step p{font-size:18px;color:var(--muted);line-height:1.45}
.how .btn{margin-top:48px}

/* advisor */
.advisor{height:940px;background:var(--blue-100);text-align:center;padding-top:92px;position:relative}
.advisor h2{font-size:52px;font-weight:700;margin-top:16px}
.advisor-card{position:absolute;left:208px;top:232px;width:792px;height:590px;background:var(--white);border-radius:8px;box-shadow:0 8px 30px rgba(0,84,170,.08);text-align:left;display:flex}
.advisor-copy{width:400px;padding:32px 24px 0 28px}
.advisor-copy p{font-size:17px;line-height:1.45;color:#1f2937;margin-bottom:18px}
.advisor-copy .btn{font-size:17px;padding:12px 26px;margin-top:6px}
.advisor-photo{position:absolute;left:400px;top:28px;width:372px;height:536px;border-radius:6px;background:linear-gradient(135deg,#2f6d4f 0%,#b9c77a 40%,#f2c94c 70%,#4d8c8a 100%)}

/* growth */
.growth{height:340px;text-align:center;padding-top:74px}
.growth h2{font-size:50px;font-weight:600}
.growth p{font-size:19px;color:var(--muted);width:780px;margin:36px auto 0;line-height:1.5}

/* footer */
.site-footer{height:316px;background:var(--navy);color:var(--white);position:relative}
.brand{position:absolute;left:36px;top:40px;display:flex;align-items:center;gap:12px}
.brand-dot{width:46px;height:46px;border-radius:50%;background:var(--blue-700)}
.brand-name{font-size:26px;font-weight:600;color:var(--orange-2)}
.footer-blurb{position:absolute;left:36px;top:112px;width:460px;font-size:17px;line-height:1.45;color:var(--blue-200)}
.footer-nav{position:absolute;top:36px;list-style:none;font-size:17px;line-height:33px}
.nav-a{left:620px}.nav-b{left:912px}
.footer-nav .btn{font-size:17px;padding:9px 20px;margin-top:4px}
.legal{position:absolute;bottom:16px;width:100%;text-align:center;font-size:12px;color:var(--blue-200);line-height:1.5}
</style>
</head>
<body>

<section class="partners">
  <span class="eyebrow">Our Trusted Partner</span>
  <div class="partner-row">
    <span class="partner">Vantor</span>
    <span class="partner">Brightline</span>
    <span class="partner">CallSphere</span>
    <span class="partner">Deskwave</span>
    <span class="partner">Nexacast</span>
  </div>
</section>

<section class="how">
  <span class="eyebrow">Here's how to</span>
  <h2>Make Tech Decisions With <em>Confidence</em></h2>
  <div class="steps">
    <div class="step">
      <svg viewBox="0 0 64 64" fill="none" stroke="#0054AA" stroke-width="3"><rect x="8" y="12" width="48" height="44" rx="4"/><path d="M8 24h48M20 6v12M44 6v12"/><path d="M22 40l7 7 13-14" stroke="#F0912C"/></svg>
      <h3>Schedule a Call</h3>
      <p>We'll take time to understand your unique needs, then determine your best next steps.</p>
    </div>
    <div class="step">
      <svg viewBox="0 0 64 64" fill="none" stroke="#0054AA" stroke-width="3"><circle cx="32" cy="32" r="26" fill="#F7CA91"/><path d="M14 48c10-6 4-16 18-16s8-12 18-18" stroke-dasharray="5 4"/><circle cx="50" cy="14" r="4" fill="#0054AA"/></svg>
      <h3>Develop a Roadmap</h3>
      <p>With our outcome-driven approach, you get a clear plan and implementation at every stage.</p>
    </div>
    <div class="step">
      <svg viewBox="0 0 64 64" fill="none" stroke="#0054AA" stroke-width="3"><rect x="8" y="8" width="48" height="40" rx="3"/><path d="M18 40V30M28 40V22M38 40V28M48 40V16" stroke="#F0912C"/><path d="M24 56h16M32 48v8"/></svg>
      <h3>Lead Future Growth</h3>
      <p>Confidently grow your business and stay ahead of disruption and the competition.</p>
    </div>
  </div>
  <span class="btn">Schedule a Call</span>
</section>

<section class="advisor">
  <span class="eyebrow">Streamline your business with</span>
  <h2>How Will an IT Advisor Help You?</h2>
  <div class="advisor-card">
    <div class="advisor-copy">
      <p>Do you really want to vet and negotiate with each service provider yourself?</p>
      <p>A trusted IT advisor reduces the time and energy it takes to source and implement tech solutions.</p>
      <p>We'll take the time to know your business and understand your needs.</p>
      <p>Then, we'll use our objective, in-depth approach to find the BEST solution for your business, at a great price.</p>
      <p>You'll walk away with a custom roadmap to easily implement your new tech solution.</p>
      <p>Plus, leverage our expert support at any time if you run into snags with your provider.</p>
      <span class="btn">Meet Our Leader, Reid</span>
    </div>
    <div class="advisor-photo" role="img" aria-label="Photo of a smiling advisor working on a laptop among green and yellow office decor"></div>
  </div>
</section>

<section class="growth">
  <h2>Secure Future Business Growth</h2>
  <p>Don't wait another day. There's too much at risk. Get the direction you need to streamline internal processes. Create an exceptional experience for customers AND employees.</p>
</section>

<footer class="site-footer">
  <div class="brand"><span class="brand-dot"></span><span class="brand-name">SkyBridge Solutions</span></div>
  <p class="footer-blurb">Helping business leaders source and implement custom technology solutions to stay ahead of disruption and outpace their competition.</p>
  <ul class="footer-nav nav-a"><li>Services</li><li>Solution</li><li>Process</li><li>Case Studies</li></ul>
  <ul class="footer-nav nav-b"><li>About</li><li>Contact</li><li>Partners</li><li><span class="btn">Schedule a Call</span></li></ul>
  <div class="legal">Copyright 2023 SkyBridge. All Rights Reserved.<br>Icons licensed from a stock library.</div>
</footer>

</body>
</html>
```